Packaging & Logo Design for Beauty product (vintage/retro/cute)

We need a Logo and packaging designed for our new product.
I have included some ideas I like for the packaging for you to get a feel of the sort of things we want.
Brand Name & Logo : Poppy & Finch (If it helps or if you think it might work, these are cats)
Product Name: Lash & Dash Eyelash Curler
Other text to go on box: People will stare, make it worth their while
Also a made with love or made by nice people stamp or logo. Please see link for the kind of things we like https://www.pictofind.example/search?q=50s+girls&src=menu&mode=img&ref=Qx7TmK2pLrNv4ZsWcYdHbA&view=1&w=1359&h=871#q=made+with+love+stamp&mode=img
The UPC Code needs to go onto the carton. Enclosed.
Carton dimensions: 12x10x4.5cm
Carton Dieline: Enclosed
Target Market(s)
Girls/ladies between the ages of 15-60

```html
<!DOCTYPE html>
<html lang="en">
<head>
<meta charset="utf-8">
<title>Poppy &amp; Finch – Lash &amp; Dash Eyelash Curler carton</title>
<link rel="stylesheet" href="https://fonts.googleapis.com/css2?family=Lobster&family=Oswald:wght@400;600&family=Comic+Neue:wght@700&display=swap">
<style>
  :root {
    --red: #e8385a;
    --mint: #cfe8e2;
    --mint-side: #c4dfd9;
    --navy: #1f2a44;
    --white: #ffffff;
    --art-light: #a9c3c3;
    --art-dark: #5b6f82;
  }
  html, body {
    margin: 0;
    padding: 0;
    width: 1200px;
    height: 1000px;
    overflow: hidden;
    background: var(--white);
  }
  .canvas {
    position: relative;
    width: 1200px;
    height: 1000px;
  }
  .carton {
    position: absolute;
    left: 194px;
    top: 200px;
    width: 812px;
    height: 600px;
    display: flex;
  }

  /* Side panel */
  .carton-side {
    position: relative;
    width: 252px;
    height: 600px;
    background: var(--mint-side);
    overflow: hidden;
  }
  .side-band {
    position: absolute;
    left: 0;
    top: 0;
    width: 252px;
    height: 220px;
  }
  .side-copy {
    position: absolute;
    left: 22px;
    right: 22px;
    top: 236px;
    color: var(--navy);
    font-family: "Oswald", sans-serif;
    font-weight: 400;
    font-size: 10px;
    line-height: 1.35;
  }
  .side-copy p {
    margin: 0;
    padding: 8px 0;
    border-bottom: 1px solid var(--navy);
  }
  .side-copy p:last-child {
    border-bottom: none;
  }
  .side-copy strong {
    font-weight: 600;
  }
  .origin-line {
    position: absolute;
    left: 22px;
    bottom: 22px;
    margin: 0;
    font-family: "Oswald", sans-serif;
    font-weight: 600;
    font-size: 10px;
    letter-spacing: 1px;
    color: var(--navy);
  }

  /* Front panel */
  .carton-front {
    position: relative;
    width: 560px;
    height: 600px;
    background: var(--mint);
    overflow: hidden;
  }
  .header-band {
    position: absolute;
    left: 0;
    top: 0;
    width: 560px;
    height: 220px;
  }
  .brand-name {
    position: absolute;
    left: 0;
    right: 0;
    top: 62px;
    margin: 0;
    text-align: center;
    font-family: "Lobster", cursive;
    font-size: 74px;
    font-weight: 400;
    line-height: 1;
    color: var(--white);
  }
  .new-badge {
    position: absolute;
    right: 24px;
    top: 148px;
    width: 76px;
    height: 76px;
    border-radius: 50%;
    background: var(--navy);
    color: var(--white);
    font-family: "Oswald", sans-serif;
    font-weight: 600;
    font-size: 22px;
    display: flex;
    align-items: center;
    justify-content: center;
    letter-spacing: 1px;
  }
  .speech-bubble {
    position: absolute;
    left: 120px;
    top: 196px;
    width: 230px;
    height: 130px;
  }
  .speech-bubble svg {
    position: absolute;
    inset: 0;
  }
  .speech-bubble p {
    position: absolute;
    left: 12px;
    right: 12px;
    top: 18px;
    margin: 0;
    text-align: center;
    font-family: "Comic Neue", sans-serif;
    font-weight: 700;
    font-size: 18px;
    line-height: 1.1;
    text-transform: uppercase;
    color: var(--navy);
  }
  .hero-illustration {
    position: absolute;
    left: 40px;
    top: 300px;
    width: 300px;
    height: 300px;
    border-radius: 130px 150px 0 0;
    background: linear-gradient(160deg, var(--art-dark) 0%, var(--art-light) 70%);
  }
  .product-info {
    position: absolute;
    left: 352px;
    top: 250px;
    width: 200px;
    text-align: center;
    color: var(--navy);
  }
  .product-name {
    margin: 0;
    font-family: "Oswald", sans-serif;
    font-weight: 600;
    font-size: 25px;
    line-height: 1.15;
    text-transform: uppercase;
    white-space: nowrap;
  }
  .tagline {
    margin: 14px 0 0;
    font-family: "Oswald", sans-serif;
    font-weight: 400;
    font-size: 17px;
  }
  .divider {
    display: block;
    margin: 6px auto;
  }
  .benefit {
    margin: 0;
    font-family: "Oswald", sans-serif;
    font-weight: 400;
    font-size: 17px;
    line-height: 1.2;
  }
  .quantity-tag {
    position: absolute;
    right: 0;
    top: 448px;
    width: 100px;
    height: 34px;
    background: var(--red);
    clip-path: polygon(0 0, 100% 0, 100% 100%, 0 100%, 10px 50%);
    color: var(--white);
    font-family: "Oswald", sans-serif;
    font-weight: 600;
    font-size: 18px;
    line-height: 34px;
    text-align: center;
    padding-left: 6px;
    box-sizing: border-box;
  }
  .product-drawing {
    position: absolute;
    left: 400px;
    top: 492px;
    width: 110px;
    height: 90px;
    border-radius: 10px;
    background: linear-gradient(180deg, #b9d6d1, #9fbfbd);
  }
</style>
</head>
<body>
<main class="canvas">
  <div class="carton">
    <aside class="carton-side">
      <svg class="side-band" viewBox="0 0 252 220" aria-hidden="true">
        <polygon points="0,0 252,0 252,210 0,150" fill="var(--red)"/>
      </svg>
      <div class="side-copy">
        <p><strong>HOW TO USE:</strong> Open the curler, place lashes between pads, close gently and hold for five seconds.</p>
        <p><strong>CAUTION:</strong> Keep out of reach of children. Do not use on wet lashes. Clean pads after each use.</p>
        <p>Replacement pads sold separately. Store in a cool, dry place away from direct sunlight.</p>
        <p>Made with love by nice people. Please recycle this carton after use.</p>
      </div>
      <p class="origin-line">MADE IN UK</p>
    </aside>

    <section class="carton-front">
      <svg class="header-band" viewBox="0 0 560 220" aria-hidden="true">
        <polygon points="0,0 560,0 560,140 0,210" fill="var(--red)"/>
      </svg>

      <h1 class="brand-name">Poppy &amp; Finch</h1>

      <div class="new-badge">NEW</div>

      <div class="speech-bubble">
        <svg viewBox="0 0 230 130" aria-hidden="true">
          <ellipse cx="115" cy="56" rx="110" ry="52" fill="var(--white)"/>
          <polygon points="150,98 176,128 170,92" fill="var(--white)"/>
        </svg>
        <p>People<br>will stare,<br>make it worth<br>their while!</p>
      </div>

      <div class="hero-illustration" role="img" aria-label="Retro line illustration of a smiling 1950s woman with pin-curled hair"></div>

      <div class="product-info">
        <h2 class="product-name">Lash &amp; Dash<br>Eyelash Curler</h2>
        <p class="tagline">high quality product</p>
        <svg class="divider" width="110" height="14" viewBox="0 0 110 14" aria-hidden="true">
          <line x1="0" y1="7" x2="44" y2="7" stroke="var(--navy)" stroke-width="1.5"/>
          <polygon points="55,1 57,5.5 62,6 58,9 59.5,13.5 55,11 50.5,13.5 52,9 48,6 53,5.5" fill="var(--navy)"/>
          <line x1="66" y1="7" x2="110" y2="7" stroke="var(--navy)" stroke-width="1.5"/>
        </svg>
        <p class="benefit">makes your eyes<br>look fabouls</p>
      </div>

      <div class="quantity-tag">1 pair</div>

      <div class="product-drawing" role="img" aria-label="Line drawing of an eyelash curler"></div>
    </section>
  </div>
</main>
</body>
</html>
```